Brevanta Website

I would like to have a revised web site for Brevanta. Brevanta is two companies - Brevanta Insurance Company and Brevanta Re Intermediaries. The logos are set, the site content is set, but the flow and look of the web site is clunky.

We do need a landing page that allows someone to choose either company. The one we have is very basic.

Current photos are not required, just ones we used.

www.brevanta-example.com is the site.

Target Market(s)

Business professionals (insurance)

Industry/Entity Type

Insurance

Requirements
Must have
• Brevanta Insurance Company
• Brevanta Re Intermediaries
• Current logos

```html
<!DOCTYPE html>
<html lang="en">
<head>
<meta charset="utf-8">
<title>Brevanta — Choose a Company</title>
<link rel="stylesheet" href="https://fonts.googleapis.com/css2?family=Montserrat:wght@400;500&family=Open+Sans:wght@400&family=Roboto:wght@400&display=swap">
<style>
  :root {
    --bg-edge: #e2e2e2;
    --bg-center: #fbfbfb;
    --frame: #bdbdbd;
    --panel-light: #ffffff;
    --panel-muted: #ebebeb;
    --navy: #1b2a38;
    --red: #de2128;
    --tagline: #7a7a7a;
    --footer: #a3a3a3;
    --white: #ffffff;
  }
  * { margin: 0; padding: 0; box-sizing: border-box; }
  html, body { width: 1200px; height: 894px; overflow: hidden; }
  body {
    position: relative;
    background: radial-gradient(ellipse 620px 520px at 600px 440px, var(--bg-center) 0%, #f1f1f1 55%, var(--bg-edge) 100%);
    font-family: "Montserrat", sans-serif;
  }
  .chooser {
    position: absolute;
    left: 194px; top: 265px;
    width: 812px; height: 366px;
    padding: 6px;
    background: var(--frame);
    border-radius: 6px;
    display: flex;
    box-shadow: 0 14px 16px -10px rgba(0,0,0,0.18);
  }
  .company {
    flex: 1;
    display: flex;
    flex-direction: column;
    align-items: center;
    text-decoration: none;
  }
  .company--re { background: var(--panel-light); border-radius: 3px 0 0 3px; }
  .company--insurance { background: var(--panel-muted); border-radius: 0 3px 3px 0; }
  .company__dot {
    width: 34px; height: 34px;
    margin-top: 82px;
    border-radius: 50%;
    background: var(--red);
  }
  .company__name {
    margin-top: 30px;
    font-weight: 400;
    font-size: 40px;
    line-height: 1;
    letter-spacing: 0.5px;
    text-transform: uppercase;
    color: var(--navy);
  }
  .company__tagline {
    margin-top: 12px;
    font-family: "Open Sans", sans-serif;
    font-size: 16px;
    letter-spacing: 4.5px;
    color: var(--tagline);
  }
  .company__enter {
    margin-top: 37px;
    width: 188px; height: 42px;
    background: var(--red);
    border-radius: 2px;
    color: var(--white);
    font-weight: 500;
    font-size: 14px;
    display: flex;
    align-items: center;
    justify-content: center;
  }
  .site-footer {
    position: absolute;
    left: 0; right: 0; top: 871px;
    text-align: center;
    font-family: "Roboto", sans-serif;
    font-size: 10px;
    color: var(--footer);
  }
  .site-footer .sep { margin: 0 7px; }
</style>
</head>
<body>
  <main class="chooser">
    <a class="company company--re" href="#">
      <span class="company__dot"></span>
      <span class="company__name">Brevanta Re</span>
      <span class="company__tagline">Intermediaries</span>
      <span class="company__enter">Click above to enter</span>
    </a>
    <a class="company company--insurance" href="#">
      <span class="company__dot"></span>
      <span class="company__name">Brevanta</span>
      <span class="company__tagline">Insurance Company</span>
      <span class="company__enter">Click above to enter</span>
    </a>
  </main>
  <footer class="site-footer">
    © 2013 www.brevanta-example.com<span class="sep">|</span>Terms of Service<span class="sep">|</span>Privacy Policy
  </footer>
</body>
</html>
```